I have a logo and need to design the business card and stationery.

The uploaded logo image named as FERNHOLT CONSTRUCTION which is to be replaced to FERNHOLT CONTRACTS. Kindly add below details and submit the designs- Company name- Fernholt Engineering Contracts LLP Name & Post- Varun Kelkar (Designated Partner) Address- Block No.712, Wing C, Tulsa Trade Court, Moti Lal Road, Pawar Industrial Estate, Goregaon(E), Mumbai - 400 063 Contact- +91 97410 58263 Email- varunkelkar@mailnest.example Website- www.fernholtcontracts.example Contact for Letterhead- +91-22-27481195

Hi Tanvir Haque, We are liking your Design #41927306. We have suggested some changes which are mentioned in feedback. Kindly revert with it asap to finalize this design.

Colors

Designer to choose colors to be used in the design.

```html
<!DOCTYPE html>
<html lang="en">
<head>
<meta charset="utf-8">
<title>Fernholt Contracts – Stationery</title>
<link href="https://fonts.googleapis.com/css2?family=Lato:wght@400;700&display=swap" rel="stylesheet">
<style>
  :root {
    --backdrop: #ededed;
    --paper: #ffffff;
    --ink: #000000;
    --ink-soft: #555555;
    --band-grey: #666666;
    --watermark: #f2f2f2;
    --shadow: 0 3px 8px rgba(0,0,0,0.28);
  }
  * { box-sizing: border-box; margin: 0; padding: 0; }
  html, body { width: 1200px; height: 1200px; overflow: hidden; }
  body { background: var(--backdrop); font-family: 'Lato', sans-serif; position: relative; }

  .sheet, .card { position: absolute; background: var(--paper); box-shadow: var(--shadow); overflow: hidden; }

  /* brand: plain square plus single-weight name */
  .brand { position: absolute; display: flex; flex-direction: column; align-items: center; }
  .brand-mark { background: var(--ink); }
  .brand-name { font-weight: 700; color: var(--ink); white-space: nowrap; line-height: 1.2; }

  /* letterhead */
  .letterhead { left: 23px; top: 114px; width: 756px; height: 973px; }
  .letterhead .brand { left: 47px; top: 44px; width: 186px; }
  .letterhead .brand-mark { width: 80px; height: 80px; margin-bottom: 14px; }
  .letterhead .brand-name { font-size: 16px; }

  .contact-list { position: absolute; list-style: none; color: var(--ink-soft); }
  .contact-list li { display: flex; align-items: center; white-space: nowrap; }
  .contact-list svg { flex: none; fill: none; stroke: var(--ink); }
  .letterhead .contact-list { left: 470px; top: 83px; border-left: 2px solid var(--band-grey); padding-left: 16px; font-size: 16px; line-height: 20.5px; }
  .letterhead .contact-list svg { width: 13px; height: 13px; margin-right: 7px; stroke-width: 2; }

  .watermark { position: absolute; left: 183px; top: 300px; width: 390px; height: 390px; background: var(--watermark); }

  .address { position: absolute; font-style: normal; color: var(--ink-soft); white-space: nowrap; }
  .address strong { color: var(--ink); font-weight: 700; display: block; }
  .letterhead .address { left: 47px; top: 858px; font-size: 16px; line-height: 20.4px; }

  .band { position: absolute; bottom: 0; }
  .band-grey { background: var(--band-grey); }
  .band-black { background: var(--ink); }
  .letterhead .band { height: 24px; }
  .letterhead .band-grey { left: 0; width: 464px; }
  .letterhead .band-black { left: 469px; right: 0; }

  /* business cards */
  .card { left: 803px; width: 375px; height: 216px; }
  .card-front { top: 369px; }
  .card-front .brand { right: 18px; top: 18px; align-items: flex-end; }
  .card-front .brand-mark { width: 85px; height: 85px; margin-bottom: 5px; }
  .card-front .brand-name { font-size: 9px; }
  .person { position: absolute; left: 16px; top: 69px; }
  .person-name { font-size: 14px; font-weight: 700; color: var(--ink); }
  .person-role { font-size: 9.5px; color: var(--ink-soft); margin-top: 1px; }
  .card-front .contact-list { left: 16px; top: 107px; font-size: 9px; line-height: 12.6px; }
  .card-front .contact-list svg { width: 8px; height: 8px; margin-right: 5px; stroke-width: 2.4; }
  .card-front .address { left: 17px; top: 150px; font-size: 9px; line-height: 12.6px; }
  .card-front .address strong { font-size: 10px; line-height: 13px; }
  .card-front .band { height: 9px; }
  .card-front .band-grey { left: 0; width: 267px; }
  .card-front .band-black { left: 272px; right: 0; }

  .card-back { top: 615px; background: var(--ink); }
  .card-back .brand { left: 0; right: 0; top: 50px; }
  .card-back .brand-mark { width: 70px; height: 70px; background: var(--paper); margin-bottom: 14px; }
  .card-back .brand-name { color: var(--paper); font-size: 15px; }
</style>
</head>
<body>

<section class="sheet letterhead">
  <div class="brand">
    <div class="brand-mark"></div>
    <div class="brand-name">FERNHOLT CONTRACTS</div>
  </div>

  <ul class="contact-list">
    <li><svg viewBox="0 0 24 24"><path d="M5 3h4l2 5-3 2a12 12 0 0 0 6 6l2-3 5 2v4a2 2 0 0 1-2 2A18 18 0 0 1 3 5a2 2 0 0 1 2-2z"/></svg>+91-22-27481195</li>
    <li><svg viewBox="0 0 24 24"><rect x="2" y="5" width="20" height="14"/><path d="M2 5l10 8 10-8"/></svg>varunkelkar@mailnest.example</li>
    <li><svg viewBox="0 0 24 24"><circle cx="12" cy="12" r="10"/><path d="M2 12h20M12 2c3 3 3 17 0 20M12 2c-3 3-3 17 0 20"/></svg>www.fernholtcontracts.example</li>
  </ul>

  <div class="watermark" aria-hidden="true"></div>

  <address class="address">
    <strong>Fernholt Engineering Contracts LLP</strong>
    Block No.712, Wing C, Tulsa Trade Court<br>
    Moti Lal Road, Pawar Industrial Estate<br>
    Goregaon(E), Mumbai - 400 063
  </address>

  <div class="band band-grey"></div>
  <div class="band band-black"></div>
</section>

<section class="card card-front">
  <div class="brand">
    <div class="brand-mark"></div>
    <div class="brand-name">FERNHOLT CONTRACTS</div>
  </div>

  <div class="person">
    <div class="person-name">VARUN KELKAR</div>
    <div class="person-role">Designated Partner</div>
  </div>

  <ul class="contact-list">
    <li><svg viewBox="0 0 24 24"><path d="M5 3h4l2 5-3 2a12 12 0 0 0 6 6l2-3 5 2v4a2 2 0 0 1-2 2A18 18 0 0 1 3 5a2 2 0 0 1 2-2z"/></svg>+91 97410 58263</li>
    <li><svg viewBox="0 0 24 24"><rect x="2" y="5" width="20" height="14"/><path d="M2 5l10 8 10-8"/></svg>varunkelkar@mailnest.example</li>
    <li><svg viewBox="0 0 24 24"><circle cx="12" cy="12" r="10"/><path d="M2 12h20M12 2c3 3 3 17 0 20M12 2c-3 3-3 17 0 20"/></svg>www.fernholtcontracts.example</li>
  </ul>

  <address class="address">
    <strong>Fernholt Engineering Contracts LLP</strong>
    Block No.712, Wing C, Tulsa Trade Court<br>
    Moti Lal Road, Pawar Industrial Estate<br>
    Goregaon(E), Mumbai - 400 063
  </address>

  <div class="band band-grey"></div>
  <div class="band band-black"></div>
</section>

<section class="card card-back">
  <div class="brand">
    <div class="brand-mark"></div>
    <div class="brand-name">FERNHOLT CONTRACTS</div>
  </div>
</section>

</body>
</html>
```